Publisher needs a book cover design for ‘Lanterns Over the Marsh Gate’ book

We need a book cover (front, back, spine) for the 2nd edition of a book entitled ‘Lanterns Over the Marsh Gate’ and subtitled ‘the quiet geography of tidal winds, ferry routes and harbour lanterns’ (inverted commas not to be part of the title and subtitle). The author is Rupert Calloway. The publisher is Vellmark Press. The finished size of the paperback version will be the industry standard 9" x 6". There will be paperback, hardback, and e-book versions. The final number of pages is expected to be in the region 150-180 pages. Text for the back cover is not yet available, but at the bottom of the back cover should be publisher logo (rectangular) on the left and space for the ISBN bar code on the right. The circular logo should be on the spine. The design should be original and not include any stock images that have been created by someone else or may require obtaining a copyright licence to use. Symbols in common use and not copyrighted are probably ok. There are no required images, photographs or symbols except the publisher logo at the left bottom of the back cover and lower spine. Spine lettering should be UK/US style with the top of the writing nearest the front cover. The designer is free to be creative using appropriate diagrams, symbols or abstract designs. Rectangular and circular variants of the publisher logo are attached. Designers are assured that when evaluating designs absolutely no notice whatsoever is taken of a designer's Pixo Rally ranking or status; We are completely output driven, so what matters is the design, not the ranking or status of the designer. In a similar way, designs are not evaluated as 'good' or 'bad' - the winning design will be chosen after review by a design review panel and is not decided arbitrarily by a single person. All submitted designs should be capable of effective copyright assignment.

Target Market(s)

Practitioners, parents, teachers, pupils and academics concerned with child protection, safeguarding and the elimination of emotional abuse of children in the classroom

Font styles to use
Serif
Sans Serif

Requirements
Must have
• • Title, author, edition, subtitle, publisher logo
Nice to have
• • Originality, innovation
Should not have
• • Stock images or anything else requiring additional copyright discussions and negotiations.

```html
<!DOCTYPE html>
<html lang="en">
<head>
<meta charset="utf-8">
<title>Lanterns Over the Marsh Gate — Cover</title>
<link rel="stylesheet" href="https://fonts.googleapis.com/css2?family=Architects+Daughter&family=Playfair+Display:ital,wght@0,400;1,400&display=swap">
<style>
  :root {
    --page: #f2f2f2;
    --navy-deep: #17203f;
    --navy: #27335f;
    --navy-soft: #34426f;
    --violet: #6e4a7e;
    --rose: #a0557c;
    --berry: #9c3d52;
    --wine: #5a1019;
    --haze: rgba(190, 196, 210, 0.55);
    --ink-light: #ffffff;
    --ink-dark: #1a1016;
    --isbn-panel: #ffffff;
  }
  * { box-sizing: border-box; margin: 0; padding: 0; }
  html, body { width: 1200px; height: 800px; overflow: hidden; background: var(--page); }
  .canvas {
    position: relative; width: 1200px; height: 800px;
    display: flex; justify-content: center; align-items: center;
  }
  .wrap {
    display: flex; height: 720px;
    box-shadow: 0 6px 24px rgba(0,0,0,0.18);
    background: linear-gradient(180deg,
      var(--navy-deep) 0%, var(--navy) 22%, var(--navy-soft) 45%,
      var(--navy) 55%, var(--violet) 66%, var(--rose) 76%,
      var(--berry) 86%, var(--wine) 100%);
  }
  .cover { position: relative; width: 470px; height: 720px; overflow: hidden; }
  .cover--front::before {
    content: ""; position: absolute; right: -80px; top: -60px;
    width: 360px; height: 260px; border-radius: 50%;
    background: radial-gradient(closest-side, var(--haze), transparent);
  }

  /* Spine */
  .spine {
    position: relative; width: 46px; height: 720px;
    border-left: 1px solid rgba(255,255,255,0.12);
    border-right: 1px solid rgba(255,255,255,0.12);
    display: flex; flex-direction: column; align-items: center;
    padding: 34px 0 30px;
  }
  .spine__text {
    writing-mode: vertical-rl;
    display: flex; align-items: center; gap: 22px;
    color: var(--ink-light); white-space: nowrap;
  }
  .spine__title { font-family: "Architects Daughter", cursive; font-size: 19px; text-transform: uppercase; }
  .spine__author { font-family: "Playfair Display", Georgia, serif; font-size: 14px; }
  .spine__logo { margin-top: auto; width: 24px; height: 24px; border-radius: 50%; background: var(--ink-dark); }

  /* Back cover */
  .blurb {
    position: absolute; left: 46px; top: 70px; width: 380px;
    font-family: "Playfair Display", Georgia, serif; font-style: italic;
    font-size: 16px; line-height: 1.45; color: var(--ink-light);
  }
  .blurb p + p { margin-top: 22px; }
  .publisher {
    position: absolute; left: 46px; bottom: 62px;
    display: flex; align-items: center; gap: 8px;
    font-family: "Playfair Display", Georgia, serif;
    font-size: 19px; letter-spacing: 0.06em; text-transform: uppercase;
    color: var(--ink-dark);
  }
  .publisher__dot { width: 26px; height: 26px; border-radius: 50%; background: var(--ink-dark); }
  .isbn-space {
    position: absolute; right: 40px; bottom: 46px;
    width: 140px; height: 84px; background: var(--isbn-panel);
  }

  /* Front cover */
  .edition {
    position: absolute; left: 36px; top: 60px;
    font-family: "Playfair Display", Georgia, serif; font-size: 14px;
    letter-spacing: 0.18em; text-transform: uppercase; color: var(--ink-light);
  }
  .author {
    position: absolute; left: 36px; top: 132px;
    font-family: "Playfair Display", Georgia, serif; font-size: 24px;
    color: var(--ink-light);
  }
  .title {
    position: absolute; left: 30px; right: 20px; top: 200px;
    font-family: "Architects Daughter", cursive; font-weight: 400;
    color: var(--ink-light); text-transform: uppercase; line-height: 1;
  }
  .title__main { display: block; font-size: 46px; letter-spacing: -0.01em; }
  .title__rest { display: block; font-size: 30px; margin: 10px 0 0 70px; }
  .artwork { position: absolute; left: 50px; top: 380px; width: 380px; height: 160px; }
  .subtitle {
    position: absolute; left: 40px; right: 40px; top: 600px;
    font-family: "Playfair Display", Georgia, serif; font-style: italic;
    font-size: 17px; line-height: 1.35; text-align: center;
    color: var(--ink-light);
  }
  .subtitle::first-letter { text-transform: uppercase; }
</style>
</head>
<body>
<main class="canvas">
  <div class="wrap">
    <section class="cover cover--back" aria-label="Back cover">
      <div class="blurb">
        <p>Lorem ipsum dolor sit amet, consectetuer adipiscing elit, sed diam nonummy nibh euismod tincidunt ut laoreet dolore magna aliquam erat volutpat. Ut wisi enim ad minim veniam, quis nostrud exerci tation ullamcorper suscipit lobortis nisl ut aliquip ex ea commodo consequat. Duis autem vel eum iriure dolor in hendrerit in vulputate velit esse molestie consequat, vel illum</p>
        <p>Lorem ipsum dolor sit amet, consectetuer adipiscing elit, sed diam nonummy nibh euismod tincidunt ut laoreet dolore magna aliquam erat volutpat. Ut wisi enim ad minim veniam, quis nostrud exerci tation ullamcorper suscipit lobortis</p>
        <p>Lorem ipsum dolor sit amet, consectetuer adipiscing elit, sed diam nonummy nibh euismod tincidunt ut laoreet dolore magna aliquam erat volutpat. Ut wisi enim ad minim veniam, quis nostrud exerci tation ullamcorper suscipit lobortis nisl ut aliquip ex ea commodo</p>
      </div>
      <div class="publisher">
        <span class="publisher__dot"></span>
        <span class="publisher__name">Vellmark Press</span>
      </div>
      <div class="isbn-space" aria-label="Space reserved for ISBN barcode"></div>
    </section>

    <section class="spine" aria-label="Spine">
      <div class="spine__text">
        <span class="spine__title">Lanterns Over the Marsh Gate</span>
        <span class="spine__author">Rupert Calloway</span>
      </div>
      <span class="spine__logo" aria-label="Vellmark Press"></span>
    </section>

    <section class="cover cover--front" aria-label="Front cover">
      <p class="edition">Second Edition</p>
      <p class="author">Rupert Calloway</p>
      <h1 class="title">
        <span class="title__main">Lanterns Over</span>
        <span class="title__rest">the Marsh Gate</span>
      </h1>
      <svg class="artwork" viewBox="0 0 380 160" role="img" aria-label="Ink line drawing of a child resting their head on folded arms at a desk">
        <defs>
          <linearGradient id="artwork-tone" x1="0" y1="0" x2="0" y2="1">
            <stop offset="0" stop-color="#3a3f66"/>
            <stop offset="1" stop-color="#7a4d80"/>
          </linearGradient>
        </defs>
        <rect x="0" y="0" width="380" height="160" fill="url(#artwork-tone)"/>
      </svg>
      <p class="subtitle">the quiet geography of tidal winds, ferry routes and harbour lanterns</p>
    </section>
  </div>
</main>
</body>
</html>
```